Missing Kids Car Doantion Website Design

Please create a new one page website design.

Current site: http://autosforyouth.net/

New WEBSITE address is: VansForLostYouth.org

Use these sites for an idea of what I am looking for. I like these sites best: tiresforsoldiers.org and autosforsoldiers.org

Coding

Coded - Design and coding required

Number of Pages Required

1 page

```html
<!DOCTYPE html>
<html lang="en">
<head>
<meta charset="utf-8">
<title>VansForLostYouth.org — Donate Your Car</title>
<link href="https://fonts.googleapis.com/css2?family=Montserrat:wght@400;600;700;800&display=swap" rel="stylesheet">
<style>
:root{
  --orange:#f36f0e;
  --yellow:#efbf4c;
  --green:#a5dc6f;
  --green-band:#b4e27b;
  --cyan:#74d5ef;
  --black:#000;
  --ink:#222;
  --grey-bg:#f3f3f3;
  --teal:#1aa7a8;
  --white:#fff;
}
*{box-sizing:border-box;margin:0;padding:0}
html,body{width:1200px;height:3495px;overflow:hidden}
body{font-family:"Montserrat",Arial,sans-serif;color:var(--ink);background:var(--white);position:relative}
.abs{position:absolute}

/* header */
.site-header{left:0;top:0;width:1200px;height:93px;background:var(--white)}
.brand{left:240px;top:34px;font-weight:700;font-size:20px;color:var(--ink);white-space:nowrap}
.header-actions{left:806px;top:33px;display:flex;gap:4px;height:26px}
.social-box{width:26px;height:26px;background:var(--black)}
.btn-donate-top{background:var(--teal);color:var(--white);font-size:11px;font-weight:700;padding:0 14px;display:flex;align-items:center;gap:6px;letter-spacing:.3px}
.main-nav{left:0;top:93px;width:1200px;height:37px;background:var(--yellow);display:flex;align-items:center;padding-left:252px;gap:28px}
.main-nav a{font-size:11px;font-weight:700;color:var(--white);text-decoration:none;text-transform:uppercase}
.main-nav a.active{color:var(--orange)}

/* hero */
.hero{left:0;top:130px;width:1200px;height:378px;background:linear-gradient(120deg,#9fb8cf 0%,#6f8fae 45%,#b0c4d6 100%)}
.hero-panel{left:121px;top:0;width:252px;height:378px;background:rgba(230,232,236,.88)}
.hero-title{left:152px;top:254px;font-size:25px;font-weight:800;line-height:1.12;color:#222;text-transform:uppercase;width:215px}
.hero-sub{left:152px;top:346px;font-size:13px;font-weight:700;color:#222}
.hero-btn{left:152px;top:368px;width:188px;height:32px;background:var(--black);color:var(--white);font-size:10px;font-weight:700;display:flex;align-items:center;justify-content:center;gap:6px}
.hero-arrow{top:174px;width:24px;height:30px;background:rgba(0,0,0,.35)}
.hero-dots{left:590px;top:360px;display:flex;gap:6px}
.hero-dots span{width:9px;height:9px;border-radius:50%;background:var(--white);opacity:.6}
.hero-dots span:first-child{opacity:1}

/* how to donate */
.section-bar{height:45px;background:var(--orange);color:var(--white);font-weight:700;font-size:14px;display:flex;align-items:center;justify-content:center}
.how-bar{left:240px;top:557px;width:720px}
.step{top:634px;width:201px;height:240px;display:flex;flex-direction:column;align-items:center;text-align:center;padding:18px 12px 0}
.step-green{left:286px;background:var(--green)}
.step-cyan{left:499px;background:var(--cyan)}
.step-yellow{left:713px;background:var(--yellow)}
.step-icon{width:58px;height:58px;border-radius:50%;background:var(--white);border:2px solid #222;display:flex;align-items:center;justify-content:center;flex:0 0 58px}
.step h3{font-size:12px;font-weight:800;margin-top:14px;line-height:1.25;color:#222}
.step h3 .phone{color:#1c44c9;white-space:nowrap}
.step p{font-size:8.5px;line-height:1.35;margin-top:6px;color:#333}
.step-btn{position:absolute;bottom:16px;left:50%;transform:translateX(-50%);width:104px;height:28px;background:var(--black);color:var(--white);font-size:9px;font-weight:700;display:flex;align-items:center;justify-content:center;gap:5px}

/* about */
.about{left:0;top:925px;width:1200px;height:595px;background:var(--green-band)}
.about-art{left:145px;top:53px;width:320px;height:373px;background:radial-gradient(circle at 50% 40%,#f2b27b 0%,#7cc35c 55%,rgba(180,226,123,0) 72%)}
.about-bar{left:485px;top:50px;width:470px;height:45px;background:var(--orange);color:var(--white);font-weight:700;font-size:14px;display:flex;align-items:center;padding-left:14px;text-transform:uppercase}
.about-text{left:487px;top:119px;width:452px;font-size:10px;line-height:1.65;color:#222}
.about-text p+p{margin-top:10px}

/* why donate */
.why{left:0;top:1520px;width:1200px;height:640px;background:var(--grey-bg)}
.why-photo{left:240px;top:48px;width:362px;height:544px;background:linear-gradient(160deg,#d9d9d9,#6b6b6b 60%,#2f2f2f)}
.why-box{left:602px;top:48px;width:358px;height:544px;border:3px solid var(--orange);background:var(--white)}
.why-head{height:45px;background:var(--orange);color:var(--white);font-weight:700;font-size:14px;display:flex;align-items:center;padding-left:14px;text-transform:uppercase}
.why-list{list-style:none;padding:18px 22px 0}
.why-list li{height:60px;margin-bottom:19px;background:#eef5e6;display:flex;align-items:center;gap:12px;padding:0 14px;font-size:9px;line-height:1.35}
.why-list li:nth-child(2),.why-list li:nth-child(5){background:#fbf0e2}
.why-list li:nth-child(4),.why-list li:nth-child(6){background:#e6f1f5}
.why-list b{font-weight:700}
.why-ico{flex:0 0 22px;height:22px;border-radius:50%}

/* missing kids */
.missing{left:0;top:2160px;width:1200px;height:630px;background:var(--black)}
.missing h2{position:absolute;left:0;width:1200px;top:58px;text-align:center;color:var(--white);font-size:23px;font-weight:700}
.kid-tile{width:226px}
.r1{top:95px;height:240px}
.r2{top:345px;height:245px}
.c1{left:247px}.c2{left:485px}.c3{left:718px}

/* stats */
.stat{top:2830px;width:400px;text-align:center}
.stat strong{display:block;font-size:23px;font-weight:700;color:#111}
.stat span{display:block;font-size:9px;color:#444;margin-top:6px}

/* faq + callout */
.faq-bar{left:12px;top:2930px;width:575px}
.faq-list{left:82px;top:3018px;list-style:none}
.faq-list li{height:65px;display:flex;align-items:flex-start;gap:12px;font-size:11px;font-weight:600;color:#222}
.faq-ico{width:22px;height:20px;background:#6cbf43;border-radius:3px}
.callout{left:600px;top:2913px;width:240px;height:571px;background:var(--orange)}
.callout-photo{left:840px;top:2913px;width:360px;height:571px;background:linear-gradient(90deg,#c46b2a 0%,#8a4a26 40%,#5d341f 100%)}
.callout-text{left:622px;top:3046px;width:205px;color:var(--white)}
.callout-text h2{font-size:25px;font-weight:700;line-height:1.15}
.callout-text h3{font-size:15px;font-weight:700;line-height:1.25;margin-top:12px}
.callout-text p{font-size:9px;line-height:1.4;margin-top:8px}
.foot-band{left:0;top:3484px;width:1200px;height:11px;background:var(--teal)}
</style>
</head>
<body>

<header class="abs site-header">
  <div class="abs brand">VansForLostYouth.org</div>
  <div class="abs header-actions">
    <span class="social-box"></span><span class="social-box"></span>
    <span class="btn-donate-top"><svg width="9" height="9" viewBox="0 0 10 10"><path d="M5 9 1 5a2.2 2.2 0 0 1 4-2.6A2.2 2.2 0 0 1 9 5z" fill="#fff"/></svg>DONATE NOW</span>
  </div>
</header>
<nav class="abs main-nav">
  <a class="active" href="#">Home</a><a href="#">About</a><a href="#">Missing Kids</a><a href="#">FAQ</a><a href="#">Contact</a>
</nav>

<section class="abs hero" role="img" aria-label="Photo of a child swinging high on a playground swing against a soft sky">
  <div class="abs hero-panel"></div>
  <div class="abs hero-arrow" style="left:8px"></div>
  <div class="abs hero-arrow" style="left:1168px"></div>
  <div class="abs hero-dots"><span></span><span></span></div>
</section>
<h1 class="abs hero-title">Donate your car to make a difference</h1>
<div class="abs hero-sub">Help Find Missing Kids</div>
<div class="abs hero-btn"><svg width="9" height="9" viewBox="0 0 10 10"><path d="M5 9 1 5a2.2 2.2 0 0 1 4-2.6A2.2 2.2 0 0 1 9 5z" fill="#fff"/></svg>DONATE NOW</div>

<div class="abs section-bar how-bar">How to donate</div>

<div class="abs step step-green">
  <div class="step-icon"><svg width="24" height="24" viewBox="0 0 24 24"><path d="M6 2h4l2 5-3 2a11 11 0 0 0 6 6l2-3 5 2v4a2 2 0 0 1-2 2A18 18 0 0 1 4 4a2 2 0 0 1 2-2z" fill="none" stroke="#222" stroke-width="1.8"/></svg></div>
  <h3>CALL US AT <span class="phone">1-888-555-0142</span><br>OR FILL OUT THE ONLINE<br>FORM</h3>
  <p>Donating your vehicle is easy and donation is accepted nationwide.</p>
  <div class="step-btn">♥ DONATE NOW</div>
</div>
<div class="abs step step-cyan">
  <div class="step-icon"><svg width="28" height="22" viewBox="0 0 30 22"><rect x="2" y="8" width="16" height="8" fill="#222"/><path d="M18 10h6l4 4v2H18z" fill="#222"/><circle cx="8" cy="18" r="3" fill="#222"/><circle cx="23" cy="18" r="3" fill="#222"/></svg></div>
  <h3>WE TOW THE<br>VEHICLE</h3>
  <p>Any vehicles are accepted and we will arrange to pick up your vehicle when it is most convenient for you.</p>
  <div class="step-btn">♥ DONATE NOW</div>
</div>
<div class="abs step step-yellow">
  <div class="step-icon"><svg width="24" height="24" viewBox="0 0 24 24"><path d="M3 16c3 0 4 2 9 2l8-4M12 3v9M9 6h5a2 2 0 0 1 0 3h-4a2 2 0 0 0 0 3h5" fill="none" stroke="#222" stroke-width="1.8"/></svg></div>
  <h3>TAX WRITE-OFF</h3>
  <p>Once the vehicle donation is complete, you will receive your tax deductible vehicle donation receipt.</p>
  <div class="step-btn">♥ DONATE NOW</div>
</div>

<section class="abs about">
  <div class="abs about-art" role="img" aria-label="Cartoon illustration of a cheerful red-haired child jumping in a green shirt"></div>
  <h2 class="abs about-bar">About Seek the Young</h2>
  <div class="abs about-text">
    <p>Seek the Young is a non-profit organization dedicated to the recovery of missing children and the prevention of the abuse and endangerment of children. We assist families searching for missing children by helping them reach local and federal law enforcement, guiding them on the right legal documents, and connecting them with other non-profit groups and community resources that may help in their search. We educate parents and children on child safety and work closely with the National Hub for Lost Youth. We have bilingual volunteers ready to work with Spanish-speaking families. Since our founding, we have assisted thousands of families by sharing flyers of missing children through our volunteer distribution program and on our stickers placed on vending machines. Our photo partner program sends children's pictures to newspapers and websites all over the country. One out of every six missing children is found through someone seeing their photo and reporting it to law enforcement. We seek to inform the public and support laws that keep our children safe.</p>
    <p>Seek the Young is the coordinating agency for the Youth Recovery Task Force, a multi-agency team sponsored by the Regional Council for Child Safety. Partners include the Harbor County Sheriff's Office, the Harbor County District Attorney's Office, city police, family services and local mental health centers working together to protect children.</p>
    <p>The Youth Recovery Task Force serves children from Harbor County who are recovered from a stranger, non-family or parental abduction and the families with whom they are reunited. The goal of the Task Force is to reduce trauma to children and their families through an effective, coordinated response to child recovery and reunification.</p>
  </div>
</section>

<section class="abs why">
  <div class="abs why-photo" role="img" aria-label="Black and white photo of a smiling boy in a cap running outdoors"></div>
  <div class="abs why-box">
    <h2 class="why-head">Why donate your car to us?</h2>
    <ul class="why-list">
      <li><span class="why-ico" style="background:#6cbf43"></span><span><b>IRS 501(C)3 Approved:</b> Free 24/7 Pickup with No DMV Hassles.</span></li>
      <li><span class="why-ico" style="background:#e89a3a"></span><span><b>Free Local Towing:</b> We will pick up your car donation, running or not, when it's most convenient, at home or work.</span></li>
      <li><span class="why-ico" style="background:#6cbf43"></span><span><b>Income Tax Deduction:</b> We issue you an IRS tax receipt and get you the highest tax write-off possible.</span></li>
      <li><span class="why-ico" style="background:#3b8fd6"></span><span><b>No Paperwork Hassles:</b> We handle everything: DMV and IRS paperwork.</span></li>
      <li><span class="why-ico" style="background:#e89a3a"></span><span><b>Car donations help fund programs.</b> And benefit Brightpath Foundation, an IRS 501(C)3 nonprofit organization.</span></li>
      <li><span class="why-ico" style="background:#e0483a"></span><span><b>Schedule a Free Pickup:</b> Complete the form and a representative will call you to arrange a convenient time to pick up your car.</span></li>
    </ul>
  </div>
</section>

<section class="abs missing">
  <h2>Missing Kids</h2>
  <div class="abs kid-tile r1 c1" style="background:linear-gradient(160deg,#ccc,#555)" role="img" aria-label="Black and white photo of a smiling boy in a cap"></div>
  <div class="abs kid-tile r1 c2" style="background:linear-gradient(160deg,#9a5a3a,#4a2a1c)" role="img" aria-label="Photo of a young girl holding a flower"></div>
  <div class="abs kid-tile r1 c3" style="background:linear-gradient(160deg,#c08a5a,#5a6a3a)" role="img" aria-label="Photo of a woman in a colorful head wrap"></div>
  <div class="abs kid-tile r2 c1" style="background:linear-gradient(160deg,#6a7a8a,#2a2e35)" role="img" aria-label="Photo of a small boy looking downward"></div>
  <div class="abs kid-tile r2 c2" style="background:linear-gradient(160deg,#5a8a6a,#2a3a2e)" role="img" aria-label="Photo of children playing in a water fountain"></div>
  <div class="abs kid-tile r2 c3" style="background:linear-gradient(160deg,#3a4a7a,#1a1e35)" role="img" aria-label="Photo of an illuminated city sign at night"></div>
</section>

<div class="abs stat" style="left:0"><strong>800,000</strong><span>children are reported missing a year</span></div>
<div class="abs stat" style="left:400px"><strong>751,000</strong><span>children have seen the Seek the Young program</span></div>
<div class="abs stat" style="left:800px"><strong>400+</strong><span>open missing children cases</span></div>

<div class="abs section-bar faq-bar">Frequently asked questions</div>
<ul class="abs faq-list">
  <li><span class="faq-ico"></span>What types of vehicles can be donated?</li>
  <li><span class="faq-ico"></span>What paperwork do I need to donate my vehicle?</li>
  <li><span class="faq-ico"></span>Is my donated vehicle tax-deductible?</li>
  <li><span class="faq-ico"></span>What if the vehicle is not registered in my name?</li>
  <li><span class="faq-ico"></span>How much will I receive as a tax deduction for my vehicle?</li>
  <li><span class="faq-ico"></span>How do I schedule a pick up?</li>
</ul>

<div class="abs callout"></div>
<div class="abs callout-photo" role="img" aria-label="Close-up photo of a young girl looking toward the viewer"></div>
<div class="abs callout-text">
  <h2>Every 10 minutes, there's an attempt to abduct a child.</h2>
  <h3>Most parents don't think it will happen to them.</h3>
  <p>You can help protect the future of children by supporting Seek the Young through your car donation. Your donated vehicle or vessel will be sold at auction and the net proceeds will be returned to Seek the Young.</p>
</div>
<div class="abs foot-band"></div>

</body>
</html>
```